Corvane Holdings , new business card design

investment firm with corporate clients . need double sided business card , vertical and horizontal options ,logo must be clear. prefer pantone colors only and sharp design. website also www.corvane-example.ae

Khalid Bin Rashed
Managing Director
Tel. +971 4 000 3829
Mobile +971 50 000 4172
khalid@corvane-example.ae
Palm Crest Tower, officw 18-B07, Qasr Gardens, Dubai

Contact Information for Business Card

Khalid Bin Rashed
Managing Director

Font styles to use
Serif

Colors

Designer to choose colors to be used in the design.

```html
<!DOCTYPE html>
<html lang="en">
<head>
<meta charset="utf-8">
<title>Corvane Holdings – Business Card</title>
<link rel="stylesheet" href="https://fonts.googleapis.com/css2?family=Alegreya:wght@400;700&display=swap">
<style>
  :root {
    --page-bg: #ffffff;
    --card-bg: #e0e0e0;
    --navy: #1b2a5e;
    --slate: #4a5677;
    --muted: #9a9ca3;
    --brand-grey: #7b8590;
  }
  * { margin: 0; padding: 0; box-sizing: border-box; }
  html, body {
    width: 1200px; height: 391px; overflow: hidden;
    background: var(--page-bg);
    font-family: "Alegreya", Georgia, serif;
  }
  .canvas { position: relative; width: 1200px; height: 391px; }
  .card {
    position: absolute; width: 529px; height: 342px;
    background: var(--card-bg);
  }
  .card--front { left: 25px; top: 27px; }
  .card--back { left: 646px; top: 22px; }

  .brand-name {
    position: absolute; left: 0; right: 0; top: 156px;
    text-align: center;
    font-size: 25px; font-weight: 400;
    letter-spacing: 0.32em;
    text-transform: uppercase;
    color: var(--brand-grey);
  }

  .brand-square {
    position: absolute; left: 28px; top: 100px;
    width: 14px; height: 14px; background: var(--navy);
  }
  .divider {
    position: absolute; left: 57px; top: 99px;
    width: 1px; height: 36px; background: var(--navy);
  }
  .holder { position: absolute; left: 71px; top: 95px; }
  .holder-name {
    font-size: 16.5px; font-weight: 700; letter-spacing: 0.12em;
    color: var(--navy); line-height: 22px;
  }
  .holder-title {
    font-size: 16.5px; letter-spacing: 0.1em;
    color: var(--slate); line-height: 22px;
  }
  .contact, .address {
    position: absolute; left: 27px;
    font-size: 14px; letter-spacing: 0.1em; line-height: 22.5px;
    color: var(--muted);
  }
  .contact { top: 153px; }
  .address { top: 241px; }
  .contact .label { color: var(--slate); margin-right: 4px; }
  .address .company { text-transform: uppercase; letter-spacing: 0.14em; }
  .website {
    position: absolute; left: 504px; top: 192px;
    transform: translate(-50%, -50%) rotate(-90deg);
    white-space: nowrap;
    font-size: 14px; letter-spacing: 0.16em;
    color: var(--navy);
  }
</style>
</head>
<body>
<div class="canvas">
  <section class="card card--front">
    <div class="brand-name">Corvane Holdings</div>
  </section>

  <section class="card card--back">
    <span class="brand-square"></span>
    <span class="divider"></span>
    <div class="holder">
      <div class="holder-name">Khalid Bin Rashed</div>
      <div class="holder-title">Managing Director</div>
    </div>
    <div class="contact">
      <div>khalid@corvane-example.ae</div>
      <div><span class="label">T</span> +971 4 000 3829</div>
      <div><span class="label">M</span> +971 50 000 4172</div>
    </div>
    <div class="address">
      <div class="company">Corvane Holdings</div>
      <div>Palm Crest Tower ∘ officw 18-B07</div>
      <div>Qasr Gardens ∘ Dubai</div>
    </div>
    <div class="website">www.corvane-example.ae</div>
  </section>
</div>
</body>
</html>
```